ink nest studio nos proporciona ter várias ideias vindo de mentes criativas diferentes o que nos faz termos muito mais variedades do que se uma única pessoa criasse vários logos.

```html
<!DOCTYPE html>
<html lang="pt-BR">
<head>
<meta charset="UTF-8">
<title>Lume Produções — Papel Timbrado</title>
<link href="https://fonts.googleapis.com/css2?family=Montserrat:wght@500;700&display=swap" rel="stylesheet">
<style>
  :root {
    --backdrop: #c9ccd1;
    --paper: #ffffff;
    --ink: #2b2b2b;
    --muted: #6d6d6d;
    --cyan: #1fb5e8;
    --green: #3cc43a;
    --red: #e8283c;
    --yellow: #f5d21a;
    --purple: #c63ad0;
    --faint: #eef2f5;
  }
  * { box-sizing: border-box; margin: 0; padding: 0; }
  html, body {
    width: 1200px; height: 1200px; overflow: hidden;
    background: var(--backdrop);
    font-family: "Montserrat", Arial, sans-serif;
  }
  .letterhead {
    position: absolute;
    left: 300px; top: 90px;
    width: 600px; height: 1020px;
    background: var(--paper);
    box-shadow: 0 10px 30px rgba(0,0,0,.18);
  }
  .brand {
    position: absolute; top: 60px; left: 0; right: 0;
    display: flex; flex-direction: column; align-items: center; gap: 10px;
  }
  .brand-dot {
    width: 26px; height: 26px; border-radius: 50%;
    background: var(--cyan);
  }
  .brand-name {
    font-weight: 700; font-size: 22px; letter-spacing: .5px;
    color: var(--ink);
  }
  .brand-watermark {
    position: absolute; left: 150px; top: 260px;
    width: 300px; height: 340px; border-radius: 40px;
    background: var(--faint);
  }
  .contact-row {
    position: absolute; left: 40px; right: 40px; bottom: 96px;
    display: flex; justify-content: space-between;
    font-size: 9px; font-weight: 500; color: var(--muted);
  }
  .contact-item { display: flex; align-items: center; gap: 6px; }
  .contact-icon { width: 10px; height: 10px; border-radius: 50%; }
  .icon-address { background: var(--cyan); }
  .icon-email { background: var(--red); }
  .icon-site { background: var(--green); }
  .icon-phone { background: var(--yellow); }
  .stripe-band {
    position: absolute; left: 0; right: 0; bottom: 30px; height: 48px;
    display: flex;
  }
  .stripe { flex: 1; }
  .stripe-cyan { background: var(--cyan); flex: .3; }
  .stripe-green { background: var(--green); }
  .stripe-red { background: var(--red); }
  .stripe-yellow { background: var(--yellow); }
  .stripe-purple { background: var(--purple); }
  .stripe-cyan-end { background: var(--cyan); flex: .3; }
  .stripe-rule {
    position: absolute; left: 0; right: 0; height: 3px; background: var(--paper);
  }
  .rule-top { bottom: 66px; }
  .rule-bottom { bottom: 40px; }
</style>
</head>
<body>
  <main class="letterhead">
    <header class="brand">
      <span class="brand-dot"></span>
      <span class="brand-name">LUME PRODUÇÕES</span>
    </header>

    <div class="brand-watermark" aria-hidden="true"></div>

    <footer>
      <div class="contact-row">
        <span class="contact-item"><span class="contact-icon icon-address"></span>Rua das Flores, 120 - Centro</span>
        <span class="contact-item"><span class="contact-icon icon-email"></span>contato@lumeproducoes.com</span>
        <span class="contact-item"><span class="contact-icon icon-site"></span>www.lumeproducoes.com</span>
        <span class="contact-item"><span class="contact-icon icon-phone"></span>(11) 4002-1234</span>
      </div>
      <div class="stripe-band">
        <span class="stripe stripe-cyan"></span>
        <span class="stripe stripe-green"></span>
        <span class="stripe stripe-red"></span>
        <span class="stripe stripe-yellow"></span>
        <span class="stripe stripe-purple"></span>
        <span class="stripe stripe-cyan-end"></span>
      </div>
      <span class="stripe-rule rule-top"></span>
      <span class="stripe-rule rule-bottom"></span>
    </footer>
  </main>
</body>
</html>
```